Business Card Design needed for logo design project

Our business needs a business card design. I'm not sure what format files are generally delivered back, but clearly I will need the ability to edit to add colleagues contact details.

Our logo is attached.

Brivomar is a 3D design services company, providing app, serious/educational game, VR and AR websites/applications to corporate clients.

Target Market(s)

Corporate blue-chip clients needing 3D design services

Industry/Entity Type

Business

Font styles to use
Sans Serif

Requirements
Must have
• Templated such that I can add details (name, phone number etc). Needs to include logo from previous project winner - attached.

```html
<!DOCTYPE html>
<html lang="en">
<head>
<meta charset="utf-8">
<title>Brivomar Business Card</title>
<link href="https://fonts.googleapis.com/css2?family=Questrial&family=Montserrat:wght@700&display=swap" rel="stylesheet">
<style>
  :root {
    --brand-red: #b51f24;
    --accent-red: #e3161c;
    --ink: #3a3a3a;
    --text: #2b2b2b;
    --paper: #ffffff;
    --backdrop: #e6e4e2;
  }
  * { margin: 0; padding: 0; box-sizing: border-box; }
  html, body { width: 1200px; height: 1000px; overflow: hidden; }
  body {
    background: var(--backdrop);
    position: relative;
    font-family: "Questrial", "Century Gothic", sans-serif;
  }
  .card {
    position: absolute;
    left: 265px;
    width: 665px;
    height: 397px;
    overflow: hidden;
    box-shadow: 0 2px 6px rgba(0,0,0,0.25);
  }
  .card-front { top: 73px; background: var(--brand-red); }
  .card-back { top: 533px; background: var(--paper); }

  .front-ring {
    position: absolute;
    left: -10px;
    top: 36px;
    width: 330px;
    height: 330px;
    border: 17px solid var(--paper);
    border-radius: 50%;
  }
  .front-wordmark {
    position: absolute;
    left: 346px;
    top: 168px;
    color: var(--paper);
    font-size: 58px;
    letter-spacing: 1px;
    line-height: 1;
  }

  .back-brand {
    position: absolute;
    left: 33px;
    top: 32px;
    display: flex;
    align-items: center;
    gap: 9px;
  }
  .brand-dot {
    width: 68px;
    height: 68px;
    border-radius: 50%;
    background: var(--accent-red);
  }
  .back-wordmark {
    color: var(--ink);
    font-size: 46px;
    letter-spacing: 0.5px;
    line-height: 1;
  }
  .person {
    position: absolute;
    left: 33px;
    top: 143px;
  }
  .person-name {
    font-family: "Montserrat", "Century Gothic", sans-serif;
    font-weight: 700;
    color: var(--accent-red);
    font-size: 21px;
    letter-spacing: 0.3px;
    line-height: 1.1;
  }
  .person-title {
    color: var(--text);
    font-size: 17px;
    margin-top: 2px;
  }
  .contact-list {
    position: absolute;
    left: 33px;
    list-style: none;
    color: var(--text);
    font-size: 16.5px;
  }
  .contact-list li {
    display: flex;
    align-items: center;
    height: 24.5px;
  }
  .contact-list svg {
    width: 14px;
    height: 14px;
    margin-right: 9px;
    fill: var(--accent-red);
    flex: none;
  }
  .phones { top: 207px; }
  .online { top: 288px; }
  .location { top: 341px; }
</style>
</head>
<body>

<section class="card card-front" aria-label="Card front">
  <div class="front-ring"></div>
  <div class="front-wordmark">BRIVOMAR</div>
</section>

<section class="card card-back" aria-label="Card back">
  <div class="back-brand">
    <div class="brand-dot"></div>
    <div class="back-wordmark">BRIVOMAR</div>
  </div>

  <div class="person">
    <div class="person-name">DANIEL HARTWELL</div>
    <div class="person-title">Executive Director</div>
  </div>

  <ul class="contact-list phones">
    <li>
      <svg viewBox="0 0 14 14" aria-hidden="true"><path d="M4 0h6a1 1 0 0 1 1 1v12a1 1 0 0 1-1 1H4a1 1 0 0 1-1-1V1a1 1 0 0 1 1-1zm0.5 1.5v10h5v-10z"/></svg>
      +61 402 518 736
    </li>
    <li>
      <svg viewBox="0 0 14 14" aria-hidden="true"><path d="M0 4c0-2 3-3 7-3s7 1 7 3v1h-3.5V3.8H3.5V5H0zM3 6h8l2 7H1zm4 1.5a2 2 0 1 0 0 4 2 2 0 0 0 0-4z"/></svg>
      +61 3 9184 2671
    </li>
    <li>
      <svg viewBox="0 0 14 14" aria-hidden="true"><path d="M3 0h8v4H3zM1 5h12a1 1 0 0 1 1 1v5h-3v3H3v-3H0V6a1 1 0 0 1 1-1zm3.5 5v2.5h5V10z"/></svg>
      +61 3 9362 4408
    </li>
  </ul>

  <ul class="contact-list online">
    <li>
      <svg viewBox="0 0 14 14" aria-hidden="true"><path d="M0 3h14v1L7 8.5 0 4zm0 2.3 7 4.5 7-4.5V11H0z"/></svg>
      daniel@brivomar.com
    </li>
    <li>
      <svg viewBox="0 0 14 14" aria-hidden="true"><path d="M7 0a7 7 0 1 0 0 14A7 7 0 0 0 7 0zm-1 1.6C5 3 4.5 4.7 4.4 6.3H1.6A5.5 5.5 0 0 1 6 1.6zm2 0a5.5 5.5 0 0 1 4.4 4.7H9.6C9.5 4.7 9 3 8 1.6zM5.9 6.3C6 4.6 6.4 3 7 1.8c.6 1.2 1 2.8 1.1 4.5zm-4.3 1.4h2.8C4.5 9.3 5 11 6 12.4a5.5 5.5 0 0 1-4.4-4.7zm4.3 0h2.2C8 9.4 7.6 11 7 12.2 6.4 11 6 9.4 5.9 7.7zm3.7 0h2.8A5.5 5.5 0 0 1 8 12.4c1-1.4 1.5-3.1 1.6-4.7z"/></svg>
      www.brivomar.com
    </li>
  </ul>

  <ul class="contact-list location">
    <li>
      <svg viewBox="0 0 14 14" aria-hidden="true"><path d="M7 0a4.8 4.8 0 0 1 4.8 4.8C11.8 8.5 7 14 7 14S2.2 8.5 2.2 4.8A4.8 4.8 0 0 1 7 0zm0 2.8a2 2 0 1 0 0 4 2 2 0 0 0 0-4z"/></svg>
      14 Kelverton Road Ashfield VIC 3810
    </li>
  </ul>
</section>

</body>
</html>
```